web site update

I want to get a better website for a small high end remodeling and construction company
I currently have a web site but you will find that it is not good.
www.quenbrickhall.com
We are a high end construction / remodeling company that has been in business since 2003. We primarily work in the mid peninsula of the bay area. Most of our clientele are very educated captains of industry. This group is still the target client.
I had my logo designed by Mint Easel a few years ago and I do like it, I like the orange and black or orange a blue. I don’t have a lot of content on hand as far as professional photographs.
Number of pages not sure and are open to: design pages vs full function website
I think what I am after is a web presence that will seal the deal as we are getting high referrals from past clients.
Construction
1 page

```html
<!DOCTYPE html>
<html lang="en">
<head>
<meta charset="utf-8">
<title>Quenbrick Hall Remodeling</title>
<link href="https://fonts.googleapis.com/css2?family=Raleway:wght@400;500;600;700&family=Roboto:wght@400;500&display=swap" rel="stylesheet">
<style>
:root{
  --orange:#f96a0e;
  --dark:#333333;
  --ink:#222222;
  --muted:#7a7a7a;
  --line:#bdbdbd;
  --band:#808080;
  --panel:#f3f3f3;
  --field:#ececec;
  --white:#ffffff;
}
*{box-sizing:border-box;margin:0;padding:0}
html,body{width:835px;height:1200px;overflow:hidden;background:var(--white)}
body{position:relative;font-family:"Raleway",sans-serif;color:var(--ink)}
.abs{position:absolute}

/* top bar */
.topbar{left:0;top:0;width:835px;height:26px;background:var(--orange);color:var(--white);font-size:7.5px}
.topbar .tagline{left:72px;top:9px}
.topbar .address{left:505px;top:8px;font-family:"Roboto",sans-serif;font-size:7px;display:flex;align-items:center;gap:4px}
.topbar .address em{font-style:italic;font-weight:500}
.social{left:666px;top:6px;display:flex;gap:6px}
.social span{width:14px;height:14px;border-radius:50%;background:rgba(255,255,255,.45)}

/* header */
.brand{left:72px;top:33px;display:flex;align-items:center;gap:7px}
.brand .mark{width:36px;height:36px;background:var(--orange)}
.brand .name{font-weight:700;font-size:11px;line-height:1.1;color:var(--orange);letter-spacing:.5px}
.contact-item{top:44px;display:flex;gap:7px;align-items:flex-start;font-size:7.2px;color:#555;line-height:1.3}
.contact-item .value{color:#333}

/* nav */
.navbar{left:0;top:81px;width:835px;height:31px;background:var(--dark)}
.nav-link{top:0;height:31px;line-height:31px;text-align:center;color:var(--white);font-size:8.5px;border-right:1px solid #555}
.nav-link.active{background:var(--orange);border-right:none}
.nav-quote{left:691px;top:0;width:73px;height:31px;line-height:31px;text-align:center;background:var(--orange);color:var(--white);font-size:8.5px}

/* hero */
.hero{left:69px;top:115px;width:699px;height:217px;background:linear-gradient(120deg,#cfc9bf 0%,#ede8df 40%,#bdb6aa 70%,#e2ddd3 100%)}
.hero-card{left:218px;top:152px;width:407px;background:rgba(70,70,70,.8);padding:6px 22px 10px 11px;color:var(--white);border-radius:2px}
.hero-card h1{font-size:20.5px;font-weight:500;white-space:nowrap;margin-bottom:5px;line-height:1.3}
.hero-card p{font-size:10.4px;font-weight:600;line-height:1.27;text-align:justify}
.hero-btn{left:346px;top:278px;width:130px;height:30px;background:var(--orange);color:var(--white);font-size:13px;font-weight:500;text-align:center;line-height:30px;border-radius:2px}
.dot{top:308px;width:13px;height:13px;border-radius:50%;background:#8a8a8a}
.dot.on{background:var(--orange);border:2px solid #8a8a8a}

/* section headings */
.sec-title{font-size:11px;font-weight:500;color:var(--ink)}
.sec-rule{height:1px;background:var(--line)}
.sec-rule::after{content:"";position:absolute;left:0;top:-1px;width:48px;height:2px;background:var(--orange)}

/* accordion */
.acc{left:69px;width:333px;height:28px;background:var(--white);box-shadow:0 1px 3px rgba(0,0,0,.18);display:flex;align-items:center;gap:8px;padding-left:6px;font-size:11px;font-weight:500}
.acc .ico{width:17px;height:17px;border-radius:50%;display:flex;align-items:center;justify-content:center}
.acc .ico.open{background:var(--orange)}
.acc .ico.closed{background:#e6e6e6}
.acc-body{left:82px;top:428px;width:300px;font-family:"Roboto",sans-serif;font-size:6.9px;line-height:1.58;color:var(--muted);text-transform:uppercase}
.acc-body p+p{margin-top:11px}

/* who we are */
.photo{background:linear-gradient(160deg,#8c8f8e,#c9b28a 55%,#3a3a3a)}
.photo.kitchen-light{background:linear-gradient(170deg,#e6e2d0,#a9a8a2 55%,#2f3236)}
.photo.cellar{background:linear-gradient(160deg,#cdc5a8,#9c8f7a 55%,#5e574f)}
.photo.bath{background:linear-gradient(170deg,#dfe0ea,#9ea4c4 45%,#f1f1f1)}
.who-title{left:605px;top:390px;width:160px;font-size:11.5px;line-height:1.2}
.who-text{left:605px;width:160px;font-family:"Roboto",sans-serif;font-size:7.2px;line-height:1.52;color:var(--muted)}
.read-more{left:602px;top:591px;width:67px;height:21px;background:var(--orange);color:var(--white);font-size:7px;text-align:center;line-height:21px;border-radius:2px}

/* gallery */
.gallery-title{left:71px;top:632px;font-size:20px;font-weight:500}
.gallery-rule{left:71px;top:658px;width:697px;height:1px;background:#999}
.gallery-rule::after{content:"";position:absolute;left:0;top:-1px;width:101px;height:2px;background:var(--orange)}
.g-label{top:815px;width:164px;text-align:center;font-size:12.5px;font-weight:500;color:#333}

/* call to action */
.cta{left:0;top:853px;width:835px;height:40px;background:var(--band)}
.cta-notch{left:403px;top:843px}
.cta-text{left:200px;top:864px;width:322px;text-align:right;white-space:nowrap;font-size:13.5px;color:var(--white)}
.cta-btn{left:535px;top:861px;width:97px;height:24px;background:var(--orange);color:var(--white);font-size:13px;text-align:center;line-height:24px;border-radius:2px}

/* testimonials */
.quote-box{left:69px;top:972px;width:334px;height:123px;background:var(--panel);padding:12px 16px;font-family:"Roboto",sans-serif;font-size:7.6px;line-height:1.45;color:#444;box-shadow:0 1px 2px rgba(0,0,0,.08)}
.quote-box p+p{margin-top:10px}
.quote-notch{left:92px;top:1095px}
.author-role{left:137px;top:1125px;font-family:"Roboto",sans-serif;font-size:7px;font-weight:500}
.author-site{left:137px;top:1137px;font-family:"Roboto",sans-serif;font-size:7px;color:#555}

/* contact form */
.field{left:432px;width:334px;background:var(--field);padding:8px 12px;font-size:8.5px;font-weight:600;color:#444}
.submit{left:432px;top:1120px;width:100px;height:21px;background:var(--orange);color:var(--white);font-size:10px;text-align:center;line-height:21px;border-radius:2px}

/* footer */
.footer{left:0;top:1173px;width:835px;height:27px;background:var(--dark);color:#bbb;font-size:8.5px}
.footer .copy{left:85px;top:8px}
.to-top{left:784px;top:1161px;width:30px;height:31px;background:var(--orange);display:flex;align-items:center;justify-content:center}
</style>
</head>
<body>

<div class="abs topbar">
  <span class="abs tagline">Some words about Bussiness</span>
  <span class="abs address">
    <svg width="7" height="9" viewBox="0 0 7 9"><path d="M3.5 0A3.3 3.3 0 0 0 .2 3.3C.2 5.8 3.5 9 3.5 9s3.3-3.2 3.3-5.7A3.3 3.3 0 0 0 3.5 0zm0 4.6a1.3 1.3 0 1 1 0-2.6 1.3 1.3 0 0 1 0 2.6z" fill="#fff"/></svg>
    simply dummy address <em>View Map</em>
  </span>
  <div class="abs social" aria-label="Social links"><span></span><span></span><span></span><span></span></div>
</div>

<header>
  <div class="abs brand">
    <span class="mark"></span>
    <span class="name">QUENBRICK HALL<br>REMODELING</span>
  </div>
  <div class="abs contact-item" style="left:398px">
    <svg width="17" height="16" viewBox="0 0 17 16"><path d="M17 0 0 7l8 1 1 8z" fill="var(--orange)"/></svg>
    <div>Our Location<br><span class="value">address city, country</span></div>
  </div>
  <div class="abs contact-item" style="left:513px">
    <svg width="16" height="14" viewBox="0 0 16 14"><path d="M1 4C1 1 15 1 15 4v2h-4V4.5H5V6H1zM3 7h10l2 7H1z" fill="var(--orange)"/><circle cx="8" cy="10.3" r="2" fill="#fff"/></svg>
    <div>Telephone Number<br><span class="value">415.555.0142</span></div>
  </div>
  <div class="abs contact-item" style="left:618px">
    <svg width="15" height="11" viewBox="0 0 15 11"><rect width="15" height="11" fill="var(--orange)"/><path d="M0 0l7.5 6L15 0" fill="none" stroke="#fff" stroke-width="1.2"/></svg>
    <div>Email Address<br><span class="value">info@quenbrickhall.com</span></div>
  </div>
</header>

<nav class="abs navbar">
  <span class="abs nav-link active" style="left:69px;width:56px">Home</span>
  <span class="abs nav-link" style="left:125px;width:75px">About Us</span>
  <span class="abs nav-link" style="left:200px;width:73px">Contact Us</span>
  <span class="abs nav-link" style="left:273px;width:80px">Gallery</span>
  <span class="abs nav-quote">Free Quote</span>
</nav>

<section>
  <div class="abs hero" role="img" aria-label="Photo of a slatted timber ceiling with radiating wood beams"></div>
  <div class="abs hero-card">
    <h1>Lorem Ipsum is simply dummy text</h1>
    <p>Lorem Ipsum is simply dummy text of the printing and typesetting industry. Lorem Ipsum has been the industry's standard dummy text ever since the 1500s, when an unknown printer took a galley of type and scrambled it to make a type specimen book.</p>
  </div>
  <div class="abs hero-btn">Send Us Quote</div>
  <span class="abs dot on" style="left:698px"></span>
  <span class="abs dot" style="left:716px"></span>
  <span class="abs dot" style="left:735px"></span>
</section>

<section>
  <h2 class="abs sec-title" style="left:70px;top:352px">WHY CHOOSE US</h2>
  <div class="abs sec-rule" style="left:69px;top:371px;width:334px"></div>

  <div class="abs acc" style="top:390px">
    <span class="ico open"><svg width="9" height="2"><rect width="9" height="2" fill="#fff"/></svg></span>
    LOREM IPSUM IS SIMPLY DUMMY TEXT
  </div>
  <div class="abs acc-body">
    <p>Lorem Ipsum is simply dummy text of the printing and typesetting industry. Lorem Ipsum has been the industry's standard dummy text ever since the 1500s, when an unknown printer took a galley of type and scrambled it to make a type specimen book. It has survived not only five</p>
    <p>essentially unchanged. It was popularised in the 1960s with the release of Letraset sheets containing Lorem Ipsum passages, and more recently with desktop publishing software like Aldus PageMaker including ver-</p>
  </div>
  <div class="abs acc" style="top:535px">
    <span class="ico closed"><svg width="9" height="9"><path d="M4.5 0v9M0 4.5h9" stroke="#888" stroke-width="1.4"/></svg></span>
    LOREM IPSUM IS SIMPLY DUMMY TEXT
  </div>
  <div class="abs acc" style="top:578px">
    <span class="ico closed"><svg width="9" height="9"><path d="M4.5 0v9M0 4.5h9" stroke="#888" stroke-width="1.4"/></svg></span>
    LOREM IPSUM IS SIMPLY DUMMY TEXT
  </div>
</section>

<section>
  <h2 class="abs sec-title" style="left:432px;top:352px">WHO WE ARE</h2>
  <div class="abs sec-rule" style="left:432px;top:371px;width:334px"></div>
  <div class="abs photo" style="left:432px;top:390px;width:154px;height:102px" role="img" aria-label="Photo of a remodeled kitchen with a city view through large windows"></div>
  <div class="abs photo kitchen-light" style="left:431px;top:513px;width:154px;height:103px" role="img" aria-label="Photo of a white kitchen with bar stools at an island"></div>
  <h3 class="abs who-title" style="font-weight:400">Lorem Ipsum is simply dummy text</h3>
  <p class="abs who-text" style="top:432px">Lorem Ipsum is simply dummy text of the printing and typesetting industry. Lorem Ipsum has been the industry's standard dummy text ever since the 1500s, when an unknown printer took a galley of type and scrambled it to make a type specimen book.</p>
  <p class="abs who-text" style="top:509px">Lorem Ipsum is simply dummy text of the printing and typesetting industry. Lorem Ipsum has been the industry's standard dummy text ever since the 1500s, when an unknown printer took a galley of type and scrambled it to make a type specimen book.</p>
  <div class="abs read-more">READ MORE</div>
</section>

<section>
  <h2 class="abs gallery-title">GALLERY</h2>
  <div class="abs gallery-rule"></div>
  <div class="abs photo cellar" style="left:69px;top:680px;width:164px;height:128px" role="img" aria-label="Photo of a stone counter over built-in wine racks"></div>
  <div class="abs photo" style="left:246px;top:680px;width:164px;height:128px" role="img" aria-label="Photo of a kitchen cooktop facing a city view"></div>
  <div class="abs photo kitchen-light" style="left:423px;top:680px;width:165px;height:128px" role="img" aria-label="Photo of a white kitchen with bar stools"></div>
  <div class="abs photo bath" style="left:601px;top:680px;width:164px;height:128px" role="img" aria-label="Photo of a bathroom vanity with blue accent tiles"></div>
  <span class="abs g-label" style="left:69px">QUENBRICK</span>
  <span class="abs g-label" style="left:246px">QUENBRICK HALL</span>
  <span class="abs g-label" style="left:423px">QUENBRICK HALL</span>
  <span class="abs g-label" style="left:601px">HALL</span>
</section>

<section>
  <div class="abs cta"></div>
  <svg class="abs cta-notch" width="32" height="11" viewBox="0 0 32 11"><path d="M0 11 16 0l16 11z" fill="var(--band)"/></svg>
  <span class="abs cta-text">Are You Looking for Constructor for your Project</span>
  <span class="abs cta-btn">Contact Us</span>
</section>

<section>
  <h2 class="abs sec-title" style="left:70px;top:925px">TESTIMONIALS</h2>
  <div class="abs sec-rule" style="left:69px;top:946px;width:334px"></div>
  <div class="abs quote-box">
    <p>Lorem Ipsum is simply dummy text of the printing and typesetting industry. Lorem Ipsum has been the industry's standard dummy text ever since the 1500s, when an unknown printer took a galley of type and scrambled it to make a type specimen book. It has survived not only five</p>
    <p>essentially unchanged. It was popularised in the 1960s with the release of Letraset sheets containing Lorem Ipsum passages, and more recently with desktop publishing software like Aldus PageMaker including versions of Lorem Ipsum.</p>
  </div>
  <svg class="abs quote-notch" width="26" height="13" viewBox="0 0 26 13"><path d="M0 0h26L13 13z" fill="var(--panel)"/></svg>
  <svg class="abs" style="left:92px;top:1122px" width="24" height="25" viewBox="0 0 24 25"><circle cx="12" cy="7" r="6" fill="#444"/><path d="M0 25c0-8 5-11 12-11s12 3 12 11z" fill="#444"/></svg>
  <span class="abs author-role">CEO</span>
  <span class="abs author-site">Northvale.com</span>
</section>

<section>
  <h2 class="abs sec-title" style="left:432px;top:925px">CONTACT US</h2>
  <div class="abs sec-rule" style="left:432px;top:946px;width:334px"></div>
  <div class="abs field" style="top:972px;height:25px">Your Name</div>
  <div class="abs field" style="top:1009px;height:25px">Your Email</div>
  <div class="abs field" style="top:1045px;height:64px">Your Message</div>
  <div class="abs submit">Submit</div>
</section>

<footer class="abs footer">
  <span class="abs copy">Copyright © 2016 quenbrickhall.com</span>
</footer>
<div class="abs to-top"><svg width="14" height="9" viewBox="0 0 14 9"><path d="M1 8 7 2l6 6" fill="none" stroke="#fff" stroke-width="2.4"/></svg></div>

</body>
</html>
```